$5 Venture Website Required

I am looking for someone to develop a website akin to the simplicity of www.filetrove.net with a video in the center or a tab that permits one to "Accept the Challenge."

Incorporates our logo and is used to promote our "$5 Venture Program."

Please see attachments, but we are igniting entrepreneurial spirit among our nation's youth through this interactive and intensive program!

There should be a way to navigate to other sections of the site including:

About
Why
Request $5 Venture Packet
Success Stories
Partners
Link to Morvan Holdings
Updates

Thanks to all in advance!

Looking forward to working with you!

Good feel of what we are looking for in terms of "feel"

http://www.brightpathwave.org/

Thank you,

RK

Please make note of this website, we are going for a feel that is akin to this and less modern and professional...more abstract and interactive...but of course include space for our video:

Colors, feel, imagery, is great. Keep your formats, but bring on the feel!

Thank you all for your hard work and patience.

Thank you all for your hard work thus far.

Meanwhile, please understand that the $5 Venture is young, youthful, full of challenge and vitality, it is a competition among students from high school and universities.  The websites you have delivered are too corporate, stale, and standard.  I'm looking for something that is fresh, different, like www.brightpathwave.org.

Symbols, cartoonish, but serious, down to business and save the world one $5 bill at a time.  The logo can be used as a theme...the colors, the feel.

Video space for explanation on the $5 Venture front and center.  With leaves, $ signs, colorful colors, etc.

Visual needs to be compelling to Join the Challenge! Although Morvan Holdings and the tree is a parent company; $5 Venture is separate and Morvan Holdings should only be mentioned as a link.

SketchHive.com in regard to simplicity; and www.brightpathwave.org in terms of style.

Thank you,

Ravinder

Like the designs that have been submitted; we are almost there.

Target Market(s)

Professors, students, teachers, parents and NGO leaders who wish to use our program as a way to inspire leadership/entrepreneurship/fundraise for their causes.

Requirements
Must have
• Place for the video, front and center
Include logo
Forsight for blogging, message, etc.
Nice to have
• Plan "buckets" to include"
Explanation Video
Two pamphlets
Contract
FAQs
Website with Blog, voting, registration, video upload, etc.
Flyer perfected
Parable...symbol of our life
Photos
Stats included
Testimonials
Organizations that have used (TLWMB, Lower Mill Forum, Corbridge High)
Sponsors (Vast Signal, Quillstone Learnerhouse)
Photos from events

I understand this takes coding and such, but want you to be aware of the long term vision for it!

```html
<!DOCTYPE html>
<html lang="en">
<head>
<meta charset="utf-8">
<title>$5 Venture</title>
<link rel="stylesheet" href="https://fonts.googleapis.com/css2?family=Roboto+Condensed:wght@300;400;700&family=Arimo:wght@400;700&display=swap">
<style>
  :root {
    --page: #dadada;
    --page-light: #e6e6e6;
    --header: #2e2e2e;
    --header-dark: #232323;
    --green: #2a9350;
    --green-dark: #1f7a40;
    --green-light: #8fe0a8;
    --ink: #1e1e1e;
    --body-text: #555555;
    --brand-text: #4a4a4a;
    --panel: #f6f6f6;
    --panel-edge: #ffffff;
    --rule: #bdbdbd;
    --white: #ffffff;
  }
  * { box-sizing: border-box; margin: 0; padding: 0; }
  html, body { width: 1200px; height: 1150px; overflow: hidden; }
  body {
    position: relative;
    background: radial-gradient(ellipse at 50% 40%, var(--page-light), var(--page) 70%);
    font-family: "Arimo", Arial, sans-serif;
    color: var(--body-text);
  }
  .site-header {
    position: absolute; left: 0; top: 0; width: 1200px; height: 134px;
    background: linear-gradient(var(--header), var(--header-dark));
  }
  .brand-banner { position: absolute; left: 41px; top: 0; width: 296px; height: 174px; }
  .brand-banner svg { position: absolute; inset: 0; }
  .brand-name {
    position: absolute; left: 0; right: 0; top: 58px; text-align: center;
    font-family: "Roboto Condensed", sans-serif; font-weight: 400;
    font-size: 34px; color: var(--brand-text);
  }
  .utility-links {
    position: absolute; top: 16px; left: 940px; display: flex; gap: 22px;
    font-family: "Roboto Condensed", sans-serif; font-weight: 700; font-size: 16px;
    color: var(--white); letter-spacing: .5px;
  }
  .language-button {
    position: absolute; left: 1062px; top: 11px; width: 102px; height: 29px;
    background: var(--green); border: 1px solid #5fbf7f;
    font-family: "Roboto Condensed", sans-serif; font-weight: 700; font-size: 13px;
    color: var(--white); padding: 6px 0 0 7px;
  }
  .language-button svg { position: absolute; right: 9px; top: 11px; }
  .main-nav {
    position: absolute; left: 441px; top: 93px; width: 751px; height: 41px;
    display: flex; border: 1px solid #444;
  }
  .main-nav a {
    display: flex; align-items: center; justify-content: center;
    background: linear-gradient(#3a3a3a, #262626); border-right: 1px solid #1a1a1a;
    font-family: "Roboto Condensed", sans-serif; font-weight: 700; font-size: 17px;
    color: var(--white); text-decoration: none; letter-spacing: .3px;
  }
  .main-nav a.is-current { color: var(--green-light); background: linear-gradient(#333, #222); }
  .section-title {
    position: absolute; font-family: "Roboto Condensed", sans-serif; font-weight: 300;
    font-size: 25px; color: var(--ink); letter-spacing: -.3px; white-space: nowrap;
  }
  .section-title strong { color: var(--green); font-weight: 700; }
  .title-rule {
    position: absolute; height: 4px;
    background: repeating-linear-gradient(90deg, #fff 0 3px, #c8c8c8 3px 5px);
  }
  .welcome-copy {
    position: absolute; left: 23px; top: 286px; width: 346px;
    font-size: 14.5px; line-height: 21px; text-align: justify;
  }
  .welcome-copy p { margin-bottom: 10px; }
  .video-panel {
    position: absolute; left: 395px; top: 196px; width: 531px; height: 443px;
    background: var(--panel); border: 1px solid var(--panel-edge);
    box-shadow: 0 2px 6px rgba(0,0,0,.2); border-radius: 4px; padding: 8px;
  }
  .video-frame {
    position: relative; width: 100%; height: 100%;
    border: 1px solid #d8d8d8; border-radius: 3px;
    background: radial-gradient(circle at 50% 45%, #eef4ec 0, #f4f4f4 45%, #e9e9e9 100%);
  }
  .video-backdrop {
    position: absolute; left: 70px; top: 20px; width: 370px; height: 370px; border-radius: 50%;
    background: radial-gradient(circle, rgba(190,220,180,.45), rgba(240,240,240,0) 70%);
  }
  .play-button { position: absolute; left: 169px; top: 89px; }
  .video-label {
    position: absolute; left: 0; right: 0; top: 296px; text-align: center;
    font-family: "Roboto Condensed", sans-serif; font-weight: 700; font-size: 34px; color: #222;
  }
  .testimonial { position: absolute; width: 172px; font-size: 15px; line-height: 20px; text-align: justify; }
  .testimonial-author { position: absolute; font-size: 15px; text-align: right; width: 150px; }
  .feature-box {
    position: absolute; top: 688px; height: 259px;
    background: var(--panel); border: 1px solid var(--panel-edge); border-radius: 4px;
    box-shadow: 0 3px 8px rgba(0,0,0,.25);
  }
  .feature-box::before {
    content: ""; position: absolute; inset: 5px; border: 2px dotted #d6d6d6; border-radius: 3px;
  }
  .feature-heading {
    position: absolute; left: 10px; right: 10px; top: 11px; height: 46px;
    background: linear-gradient(var(--green), var(--green-dark));
    border-top: 2px dashed #7acb93; border-bottom: 2px dashed #7acb93;
    font-family: "Roboto Condensed", sans-serif; font-weight: 700; font-size: 23px;
    color: var(--white); padding: 7px 0 0 14px; text-shadow: 0 1px 2px rgba(0,0,0,.4);
  }
  .photo-thumb {
    position: absolute; top: 94px; width: 152px; height: 126px; background: #fff;
    border: 1px solid #d4d4d4; border-radius: 8px; box-shadow: 0 3px 6px rgba(0,0,0,.18); padding: 10px;
  }
  .photo-thumb div { width: 100%; height: 100%; background: linear-gradient(135deg, #6fb4d8, #7bc043 50%, #e4c12d); }
  .feature-text { position: absolute; font-size: 14.5px; line-height: 21px; text-align: justify; }
  .blog-entry { font-size: 14px; text-align: left; width: 278px; }
  .read-more {
    position: absolute; right: 10px; bottom: 10px; width: 96px; height: 33px;
    background: var(--green); color: var(--white); font-size: 14px;
    display: flex; align-items: center; justify-content: center;
  }
  .blog-divider { position: absolute; left: 16px; right: 16px; top: 137px; border-top: 1px dotted #999; }
  .site-footer-rule { position: absolute; left: 23px; top: 1017px; width: 1151px; border-top: 2px dotted var(--rule); }
  .footer-brand {
    position: absolute; left: 40px; top: 1048px;
    font-family: "Roboto Condensed", sans-serif; font-weight: 400; font-size: 22px; color: var(--brand-text);
  }
  .footer-links { position: absolute; right: 40px; top: 1038px; display: flex; gap: 20px; font-size: 14px; color: #333; }
  .copyright { position: absolute; right: 40px; top: 1066px; font-size: 14px; color: #333; }
</style>
</head>
<body>
  <header class="site-header">
    <div class="brand-banner">
      <svg width="296" height="174" viewBox="0 0 296 174">
        <path d="M0 0H296V172L148 150L0 172Z" fill="#f2f2f2"/>
        <path d="M8 0H288V160L148 140L8 160Z" fill="#fff" stroke="#d0d0d0" stroke-width="2"/>
      </svg>
      <div class="brand-name">$5 Venture</div>
    </div>
    <nav class="utility-links"><span>FAQ</span><span>SIGNIN</span></nav>
    <div class="language-button">LANGUAGE
      <svg width="12" height="9" viewBox="0 0 12 9"><path d="M0 0H12L6 9Z" fill="#0d4a22"/></svg>
    </div>
    <nav class="main-nav">
      <a class="is-current" style="width:69px">HOME</a>
      <a style="width:106px">ABOUT US</a>
      <a style="width:132px">WHY WE ARE?</a>
      <a style="width:168px">SUCCESS STORIES</a>
      <a style="width:111px">PARTNERS</a>
      <a style="width:165px;border-right:0">MORVAN HOLDINGS</a>
    </nav>
  </header>

  <h1 class="section-title" style="left:23px;top:222px">WELCOME TO <strong>$5 VENTURE</strong></h1>
  <div class="title-rule" style="left:23px;top:263px;width:346px"></div>
  <div class="welcome-copy">
    <p>Lorem ipsum dolor sit amet, consectetur adipiscing elit. Curabitur eu nisl odio. Cras egestas turpis in mi feugiat vel tincidunt arcu accumsan. Phasellus non posuere eros. Aenean consectetur.</p>
    <p>sapien in elit luctus ac posuere purus placerat. Aliquam turpis lorem,.</p>
    <p>Donec fermentum sodales erat, quis consequat nisi ornare eget. Duis volutpat justo ut ante imperdiet feugiat. fermentum sodales erat, quis consequat nisi ornare eget. Duis volutpat justo ut ante imperdiet feugiat.</p>
    <p>sapien in elit luctus ac posuere purus placerat. Aliquam turpis lorem,.</p>
  </div>

  <section class="video-panel">
    <div class="video-frame">
      <div class="video-backdrop" role="img" aria-label="Soft leaf motif behind the video"></div>
      <svg class="play-button" width="176" height="176" viewBox="0 0 176 176">
        <circle cx="88" cy="88" r="87" fill="#1b1b1b"/>
        <circle cx="88" cy="88" r="80" fill="#2c2c2c"/>
        <path d="M70 54L118 88L70 122Z" fill="#e8e8e8"/>
      </svg>
      <div class="video-label">WATCH VIDEO</div>
    </div>
  </section>

  <h2 class="section-title" style="left:956px;top:222px"><strong>CLIENT</strong> TESTIMONIALS</h2>
  <div class="title-rule" style="left:956px;top:263px;width:218px"></div>
  <p class="testimonial" style="left:983px;top:318px">Lorem ipsum dolor sit amsectetur adipiscing elit. Curabitur eu nisl odio. dolor sit amsectetur u nisl odio.</p>
  <div class="testimonial-author" style="left:1024px;top:426px">- LOREM IPSUM</div>
  <p class="testimonial" style="left:979px;top:491px">Lorem ipsum dolor sit amsectetur adipiscing elit. Curabitur eu nisl odio. dolor sit amsectetur u nisl odio.</p>
  <div class="testimonial-author" style="left:1024px;top:597px">- LOREM IPSUM</div>

  <section class="feature-box" style="left:26px;width:474px">
    <h3 class="feature-heading">PHOTO</h3>
    <svg style="position:absolute;left:22px;top:92px" width="22" height="110" viewBox="0 0 22 110"><path d="M20 2L4 55L20 108" fill="none" stroke="#d0d0d0" stroke-width="4"/></svg>
    <div class="photo-thumb" style="left:66px"><div role="img" aria-label="Event photo of students building a puzzle"></div></div>
    <div class="photo-thumb" style="left:246px"><div role="img" aria-label="Event photo of students building a puzzle"></div></div>
    <svg style="position:absolute;right:22px;top:92px" width="22" height="110" viewBox="0 0 22 110"><path d="M2 2L18 55L2 108" fill="none" stroke="#d0d0d0" stroke-width="4"/></svg>
  </section>

  <section class="feature-box" style="left:532px;width:308px">
    <h3 class="feature-heading">LATEST NEWS</h3>
    <svg style="position:absolute;left:23px;top:100px" width="12" height="10" viewBox="0 0 12 10"><path d="M0 0L5 5L0 10ZM6 0L11 5L6 10Z" fill="#333"/></svg>
    <p class="feature-text" style="left:48px;top:92px;width:244px">Lorem ipsum dolor sit amet, consectetur adipiscing elit. Curabitur eu nisl odio. Lorem ipsum dolor sit amet, consectetur adipiscing elit. Curabitur eu nisl odio.</p>
    <div class="read-more">READ MORE</div>
  </section>

  <section class="feature-box" style="left:866px;width:308px">
    <h3 class="feature-heading">BLOG</h3>
    <p class="feature-text blog-entry" style="left:24px;top:84px">Lorem ipsum dolor sit amet, consectetur adipiscing elit. Curabitur eu nisl odio.</p>
    <div class="blog-divider"></div>
    <p class="feature-text blog-entry" style="left:28px;top:150px">Lorem ipsum dolor sit amet, consectetur adipiscing elit. Curabitur eu nisl odio.</p>
    <div class="read-more">READ MORE</div>
  </section>

  <footer>
    <div class="site-footer-rule"></div>
    <div class="footer-brand">$5 Venture</div>
    <nav class="footer-links">
      <span>Home</span><span>About Us</span><span>Success Stories</span><span>Partners</span><span>Morvan Holdings</span><span>Terms</span><span>Privacy Policy</span>
    </nav>
    <div class="copyright">All Rights reserved @ $5venture</div>
  </footer>
</body>
</html>
```